Book Cover Design for a Romantic Comedy Novel

Hi there,

we are two German authors planning to digitally publish our first novel. In order to draw a lot of attention to our e-book we need an eye-catching cover design. That is where we need your help!

Here is the novel's synopsis:
Marie, a 29-year-old business analyst from Stuttgart, knows exactly what the man of her life should not be like: no colleague, no workaholic, no smoker and nobody with a tattoo. When she learns that her ex-boyfriend is going to marry, she throws all her caution overboard and spends the night with a man she has just met. Monday morning she is in for a surprise: her one-time lover turns out to be her new colleague! And in every other aspect, too, Karlo seems to be the embodiment of Marie's no-go-list.

The character's looks: Marie is tall, has long red curls and light skin. Karlo is also tall and has very short light brown hair.

The title of the book is "Vergessen verzaubert" which cannot be translated into English without losing some of its meaning.

While "verliebt" is best translated with "in love", the German word "verplant" has two meanings:
a) over-scheduled, making too many plans (Marie loves to make plans and to write lists like her no-go-list, to-do-lists ...)
b) to be out of it (Marie does not recognize her Mr Perfect when he stands right before her eyes)

Our names should also be on the cover: Annika Falter & Henriette Dussel

Please note the technical requirements below.

We are looking forward to your great designs.
Thanks
Annika & Henriette
Updates

Hi there, we just added some book covers to our project in order to show you the kind of design we generally like. Of course, we do not want to limit your creativity - so feel free to post something different. Furthermore, we added some details on the look of our main characters in case you want to show them on your cover. Thank you very much for your contributions so far! BR Henriette & Annika

Target Market(s)

Women aged 25 to 40

Industry/Entity Type

Business

Requirements
Must have
• This is a book for women, romantic, funny & smart. So please stick to the genre, the cover has to show on first glance what to expect.

Technical requirements:

1. The cover needs to be legible and good-looking when it is reduced to a small icon the size of a stamp. This will be the case when the book cover is shown in a list with lots of other book covers.

2. The design should be in colour, but it should also work in black and white as a lot of e-book readers do not display colours.

3. We need a jpeg with the following measurements: ratio = 16:10, the longer side with at least 2500 pixel.

4. As we want to publish our book in several online bookstores and maybe one day as a printed version, we ask you to provide us the original photoshop-file. Each digital bookstore has different requirements with regards to file size and width-to-heigth-ratio. Therefore, the cover design should be scalable to different ratios.

Should not have
• We do not want a book cover based on a real photograph.

```html
<!DOCTYPE html>
<html lang="de">
<head>
<meta charset="utf-8">
<title>Vergessen verzaubert – Roman</title>
<link rel="stylesheet" href="https://fonts.googleapis.com/css2?family=Cinzel:wght@400&family=Pinyon+Script&display=swap">
<style>
  :root {
    --parchment-light: #f8e6bf;
    --parchment-mid: #efcb8e;
    --parchment-edge: #dc9f62;
    --heart-red: #b3221c;
    --heart-deep: #8c1412;
    --author-red: #a8281e;
    --title-ink: #120c08;
  }
  * { margin: 0; padding: 0; box-sizing: border-box; }
  html, body {
    width: 802px;
    height: 1200px;
    overflow: hidden;
    background: #ffffff;
  }
  .cover {
    position: relative;
    width: 802px;
    height: 1200px;
    overflow: hidden;
    background: radial-gradient(ellipse at 38% 38%, var(--parchment-light) 0%, var(--parchment-mid) 62%, var(--parchment-edge) 100%);
  }
  .cover__hearts {
    position: absolute;
    inset: 0;
    width: 802px;
    height: 1200px;
  }
  .cover__authors {
    position: absolute;
    left: 104px;
    top: 46px;
    font-family: "Cinzel", serif;
    font-size: 42px;
    line-height: 58px;
    letter-spacing: 1px;
    color: var(--author-red);
    text-transform: uppercase;
  }
  .cover__title {
    position: absolute;
    left: 30px;
    top: 262px;
    font-family: "Pinyon Script", cursive;
    font-weight: 400;
    color: var(--title-ink);
    font-size: 146px;
    line-height: 168px;
  }
  .cover__title-line { display: block; }
  .cover__title-line--second { padding-left: 100px; }
  .cover__genre {
    position: absolute;
    left: 104px;
    top: 958px;
    font-family: "Cinzel", serif;
    font-size: 40px;
    letter-spacing: 1px;
    color: var(--author-red);
  }
</style>
</head>
<body>
  <main class="cover">
    <svg class="cover__hearts" viewBox="0 0 802 1200" role="img" aria-label="Cascade of painted red hearts rising along the right edge and across the bottom of the parchment">
      <defs>
        <linearGradient id="heart-band" x1="0" y1="0" x2="1" y2="0.3">
          <stop offset="0" stop-color="#b3221c" stop-opacity="0.55"/>
          <stop offset="0.45" stop-color="#b3221c" stop-opacity="0.9"/>
          <stop offset="1" stop-color="#8c1412"/>
        </linearGradient>
      </defs>
      <path d="M802 0 L720 0 C690 120 700 260 640 380 C600 470 640 600 600 720 C540 800 380 860 330 980 C300 1060 250 1130 180 1200 L802 1200 Z" fill="url(#heart-band)"/>
    </svg>
    <p class="cover__authors">Annika Falter &amp;<br>Henriette Dussel</p>
    <h1 class="cover__title">
      <span class="cover__title-line">Vergessen</span>
      <span class="cover__title-line cover__title-line--second">verzaubert</span>
    </h1>
    <p class="cover__genre">ROMAN</p>
  </main>
</body>
</html>
```